"Copper Lantern" Hot Sauce Label

To touch up (and possibly add material to) our existing hot sauce bottle labels.

We want to be a bit more professional while maintaining a DIY fee...

Target Market(s)

Hipster Foodies, Chili Lovers, Farmers Market goers, Whole and Natural Food Grocery Store Shoppers.

Industry/Entity Type

Food Production

Requirements
Must have
• A D-I-Y Feel- look professional, texts are very important to us. It needs to be simple, clean, and not over burdened over "Busy".
Nice to have
• A Folklorish or Fantasy type feel.
Should not have
• Distracting Colors and Fonts

```html
<!DOCTYPE html>
<html lang="en">
<head>
<meta charset="utf-8">
<title>Copper Lantern – Fermented Pepper Sauce Label</title>
<link rel="stylesheet" href="https://fonts.googleapis.com/css2?family=Special+Elite&family=Courier+Prime:wght@400;700&display=swap">
<style>
  :root {
    --backdrop: #3b3a35;
    --paper: #ffffff;
    --ink: #1a1a1a;
    --band-green: #3a9b35;
    --band-text: #ffffff;
    --divider: #b5b5b5;
    --art-light: #ececec;
    --art-dark: #6a6a6a;
  }
  * { margin: 0; padding: 0; box-sizing: border-box; }
  html, body {
    width: 1200px; height: 1000px; overflow: hidden;
    background: var(--backdrop);
  }
  .label {
    position: absolute; left: 186px; top: 136px;
    width: 824px; height: 729px;
    background: var(--paper);
    display: flex;
    color: var(--ink);
    font-family: "Special Elite", "Courier Prime", monospace;
  }
  .front-panel, .back-panel {
    position: relative; width: 412px; height: 100%;
  }
  .back-panel { border-left: 1px solid var(--divider); text-align: center; }

  .figure-art {
    position: absolute; left: 50px; top: 18px;
    width: 310px; height: 552px;
    background: radial-gradient(ellipse at 50% 45%, var(--art-dark) 0%, #9a9a9a 45%, var(--art-light) 80%, var(--paper) 100%);
    border-radius: 4px;
  }

  .name-band {
    position: absolute; left: 0; bottom: 0;
    width: 100%; height: 145px;
    background: var(--band-green);
    color: var(--band-text);
    text-align: center;
    padding-top: 20px;
  }
  .product-name { font-size: 40px; font-weight: 400; letter-spacing: 1px; line-height: 1.1; }
  .product-type { font-family: "Courier Prime", monospace; font-weight: 700; font-size: 25px; margin-top: 4px; }
  .net-size { font-family: "Courier Prime", monospace; font-weight: 700; font-size: 14px; margin-top: 2px; }

  .story {
    position: absolute; top: 26px; left: 0; width: 100%;
    font-size: 17px; line-height: 23px;
  }
  .rally { position: absolute; top: 214px; left: 0; width: 100%; font-size: 17px; }

  .farm-mark {
    position: absolute; top: 252px; left: 0; width: 100%; height: 200px;
    display: flex; align-items: center; justify-content: center; gap: 14px;
  }
  .farm-dot {
    width: 120px; height: 120px; border-radius: 50%;
    border: 2px solid var(--ink);
    flex: none;
  }
  .farm-name { font-size: 19px; letter-spacing: 0.5px; }

  .ingredients {
    position: absolute; top: 468px; left: 0; width: 100%;
    font-size: 16px; line-height: 15px;
  }
  .lot { position: absolute; top: 600px; left: 102px; font-size: 18px; font-weight: 700; font-family: "Courier Prime", monospace; }
  .storage { position: absolute; top: 652px; left: 0; width: 100%; font-size: 13px; }
  .address { position: absolute; top: 672px; left: 0; width: 100%; font-size: 17px; line-height: 15px; }
</style>
</head>
<body>
  <div class="label">
    <section class="front-panel">
      <div class="figure-art" role="img" aria-label="Engraved illustration of a classical robed goddess holding a tall staff and a sprig of herbs"></div>
      <div class="name-band">
        <h1 class="product-name">COPPER LANTERN</h1>
        <p class="product-type">Fermented Pepper Sauce</p>
        <p class="net-size">5 fl. oz (142 g)</p>
      </div>
    </section>

    <section class="back-panel">
      <p class="story">Inspired by the last peppers<br>of the Season picked right<br>before the first frost..<br>Green, Smokey and Fierce,<br>just the right amount<br>of Garlic, Lemon<br>and Brown Sugar.</p>
      <p class="rally">Long live the Copper Lantern!</p>

      <div class="farm-mark">
        <span class="farm-dot"></span>
        <span class="farm-name">Hollow Oak Farms</span>
      </div>

      <p class="ingredients">Ingredients:<br>Green Peppers, Tomatoes,<br>Apple Cider Vinegar,<br>Garlic, Smoked Sea Salt,<br>Organic Brown Sugar,<br>Pink Salt, Lemon.</p>

      <p class="lot">Lot:</p>
      <p class="storage">Keep Refrigerated</p>
      <p class="address">418 Alder Lane,<br>Fairbrook VA, 23000</p>
    </section>
  </div>
</body>
</html>
```